Hi Marta,
can you please design business cards for me?
Based on your Velbrandt design please go crazy (still retain a professional business-solid profile). I would like to use really stylish paper (or different paper types and special prints like partly embossed or partly glossy and contrast the glossiness with matt for instance).
Please keep in mind that I might come back to you in several months if the business requires other print material like stationary, folders, envelopes etc. It all needs to be in line and make a huge impression without going over board and still remain very solid and serious.
I know that's a lot to ask and I apologise but I am really impressed with your work so far and have no doubt that you can spin the wheels again in a great way.
Thanks bunches, Lukas
In order to punch in the right text from the outset, here is some key data:
Velbrandt
Your next level
Lukas Ferber
Head of Forward Momentum
+41 76 830 1474
lukas.ferber@velbrandt-example.com
velbrandt-example.com
Business
Velbrandt
Your next level
Lukas Ferber
+41 76 830 1474
velbrandt-example.com

```html
<!DOCTYPE html>
<html lang="en">
<head>
<meta charset="utf-8">
<title>Lukas Ferber – Business Card</title>
<link rel="stylesheet" href="https://fonts.googleapis.com/css2?family=Lato:wght@300;400;700&display=swap">
<style>
  :root {
    --backdrop: #5a5a5a;
    --card-orange: #d8862b;
    --card-paper: #d9d4d3;
    --ink-dark: #3b302b;
    --ink-soft: #5b5250;
    --disc-light: #fbfaf8;
  }
  * { box-sizing: border-box; margin: 0; padding: 0; }
  html, body { width: 1200px; height: 895px; overflow: hidden; }
  body {
    background: var(--backdrop);
    font-family: "Lato", sans-serif;
    position: relative;
  }
  .card {
    position: absolute;
    top: 185px;
    width: 340px;
    height: 525px;
    box-shadow: 0 12px 28px rgba(0,0,0,0.35);
  }
  .card-front { left: 200px; background: var(--card-orange); }
  .card-back { left: 660px; background: var(--card-paper); text-align: center; }

  .monogram {
    position: absolute;
    left: 50%;
    transform: translateX(-50%);
    border-radius: 50%;
    display: flex;
    align-items: center;
    justify-content: center;
    font-weight: 300;
    letter-spacing: -1px;
  }
  .card-front .monogram {
    top: 110px;
    width: 100px; height: 100px;
    background: var(--disc-light);
    border: 8px solid var(--ink-dark);
    color: var(--ink-dark);
    font-size: 32px;
  }
  .card-back .monogram {
    top: 110px;
    width: 92px; height: 92px;
    background: var(--ink-dark);
    border: 5px solid var(--card-orange);
    color: var(--disc-light);
    font-size: 30px;
  }

  .identity {
    position: absolute;
    top: 232px;
    left: 0; right: 0;
  }
  .person-name {
    display: inline-block;
    font-weight: 700;
    font-size: 21px;
    letter-spacing: 2px;
    color: var(--ink-dark);
    padding-bottom: 4px;
    border-bottom: 1px solid var(--card-orange);
  }
  .person-role {
    margin-top: 5px;
    font-size: 13px;
    font-weight: 400;
    color: var(--ink-soft);
    letter-spacing: 0.3px;
  }
  .contact {
    position: absolute;
    top: 330px;
    left: 0; right: 0;
    list-style: none;
    font-size: 14px;
    line-height: 19px;
    color: var(--ink-soft);
    letter-spacing: 0.4px;
  }
</style>
</head>
<body>
  <section class="card card-front" aria-label="Card front">
    <div class="monogram">LF</div>
  </section>

  <section class="card card-back" aria-label="Card back">
    <div class="monogram">LF</div>
    <div class="identity">
      <h1 class="person-name">LUKAS FERBER</h1>
      <p class="person-role">Head of Forward Momentum</p>
    </div>
    <ul class="contact">
      <li class="contact-phone">+41 76 830 1474</li>
      <li class="contact-web">velbrandt-example.com</li>
      <li class="contact-email">lukas.ferber@velbrandt-example.com</li>
    </ul>
  </section>
</body>
</html>
```